Business Card Design for drone videography and photography

I have a Vorkel Skyra 3 drone. I am looking for a logo to somehow incorporate with my business name. I don't even know what is an appropriate font. I am most filming real estate homes. I want something simplistic and a logo that makes sense for the business that I'm in. xxxxxxxxxxxxxxxxxxxxxxxxxxxxxxxxxxxxxxxxxxxxxxxxxxxxxxxxxxxxxxxxxxxxxxxxxxxxxxxxxxxxxxxxxxxxxxxxxxxxxxxxxxxxxxxxxxxxxxxxxxxxxxxxxxxxxxxxxxxxxxxxxxxxxxxxxxxxxxxxxxxxxxxxxxxxxxxxxxxxxxxxxxxxxxxxxxxxxxxxxxxxxxxxxxxxxxxxxxxxxxxxxxxxxxxxxxxxxxxxxxxxxxxxxxxxxxxxxxxxxxxxxxxxxxxxxxxxxxxxxxxxxxxxxxxxxxxxxxxxxxxxxxxxxxxxxxxxxxxxxxxxxxxxxxxxxxxxxxxxxxxxxxxxxxxxxxxxxxxxxxxxxxxxxxxxxxxxxxxxxxxxxxxxxxxxxxxxxxxxxxxxxxxxxxxxxxxxxxxxxxxxxxxxxxxxxxxxxxxxxxxxxxxxxxxxxxxxxxxxxxxxxxxxxxxxxxxxxxxxxxxxxxxxxxxxxxxxxxxxxxxxxxxxxxxxxxxxxxxxxxxxxxxxxxxxxxxxxxxxxxxxxxxxxxxxxxxxxxxxxxxxxxxxxxxxxxxxxxxxxxxxxxxxxxxxxxxxxxxxxxxxxxxxxxxxxxxxxxxxxxxxxxxxxxxxxxxxxxxxxxxxxxxxxxxxxxxxxxxxxxxxxxxxxxxxxxxxxxxxxxxxxxxxxxxxxxxxxxxxxxxxxxxxxxxxxxxxxxxxxxxxxxxxxxxxxxxxxxxxxxxxxxxxxxxxxxxxxxxxxxxxxxxxxxxxxxxxxxxxxxxxxxxxxxxxxxxxxxxxxxxxxxxxxxxxxxxxxxxxxxxxxxxxxxxxxxxxxxxxxxxxxxxxxxxxxxxxxxxxxxxxxxxxxxxxxxxxxxxxxxxxxxxxxxxxxxxxxxxxxxxxxxxxxxxxxxxxxxxxxxxxxxxxxxxxxxxxxxxxxxxxxxxxxxxxxxxxxxxxxxxxxxxxxxxxxxxxxxxxxxxxxxxxxxxxxxxxxxxxxxxxxxxxxxxxxxxxxxxxxxxxxxxxxxxxxxxxxxxx

Target Market(s)

Real estate

Industry/Entity Type

Business

Contact Information for Business Card

TRASK AERIAL IMAGING
Daniel Trask
Owner/Operator

40528 Birchwood Ct.
Harlow Springs KS 63514

314-555-0187
dtrask@traskaerialimaging.com

NAB Drone Certified
Insured
Section 333 Exempt
Vexo Flight Class Certified

Font styles to use
Other font styles liked:
• PUMP DEMI BOLD LET

Requirements
Must have
• Maybe have the certifications on the back??? The business card must be more serious than playful
Nice to have
• Possibly have the logo work itself into the business name?
Should not have
• nothing that looks like a "fun" business. I want this business card to look professional but also simplistic. I don't want a picture that I took from my drone as the background.

```html
<!DOCTYPE html>
<html lang="en">
<head>
<meta charset="utf-8">
<title>Trask Aerial Imaging – Business Card</title>
<link rel="stylesheet" href="https://fonts.googleapis.com/css2?family=Questrial&display=swap">
<style>
  :root {
    --page-bg: #e9e9e9;
    --card-white: #fbfbfb;
    --ink: #1c1c1c;
    --band-dark: #2f3133;
    --band-dark-2: #45484b;
    --blue-deep: #1a5f93;
    --blue-mid: #2586b8;
    --blue-light: #3bb1d6;
    --accent: #3aaad3;
    --rule: rgba(255,255,255,0.35);
    --text-light: #ffffff;
  }
  * { box-sizing: border-box; margin: 0; padding: 0; }
  html, body {
    width: 720px; height: 1200px; overflow: hidden;
    background: var(--page-bg);
    font-family: "Questrial", sans-serif;
  }
  .sheet {
    width: 720px; height: 1200px;
    display: flex; flex-direction: column; align-items: center; justify-content: center;
    gap: 40px;
  }
  .card {
    width: 310px; height: 542px;
    position: relative; overflow: hidden;
    box-shadow: 0 6px 18px rgba(0,0,0,0.18);
  }

  /* Brand lockup */
  .brand {
    display: flex; flex-direction: column; align-items: center; gap: 10px;
  }
  .brand-dot {
    width: 14px; height: 14px; border-radius: 50%;
    background: var(--accent);
  }
  .brand-name {
    color: var(--ink);
    font-size: 17px; letter-spacing: 4px; text-align: center; line-height: 1.5;
  }

  /* Front */
  .card-front { background: var(--card-white); }
  .front-top {
    height: 290px; display: flex; align-items: center; justify-content: center;
  }
  .name-band {
    height: 62px; display: flex;
    background: linear-gradient(90deg, var(--band-dark), var(--band-dark-2));
  }
  .icon-cell {
    width: 62px; flex: none; display: flex; align-items: center; justify-content: center;
  }
  .icon-cell svg { width: 24px; height: 24px; fill: var(--text-light); }
  .name-block { display: flex; flex-direction: column; justify-content: center; gap: 3px; }
  .person-name { color: var(--text-light); font-size: 20px; }
  .person-role { color: var(--accent); font-size: 13px; letter-spacing: 1px; }
  .contact-list {
    list-style: none; height: 190px;
    background: linear-gradient(135deg, var(--blue-deep), var(--blue-mid) 55%, var(--blue-light));
  }
  .contact-row {
    height: 63px; display: flex; align-items: center;
    border-bottom: 1px solid var(--rule);
    color: var(--text-light); font-size: 13px; line-height: 1.45;
  }
  .contact-row:last-child { border-bottom: none; }
  .contact-row .icon-cell { background: rgba(0,0,0,0.12); height: 100%; }
  .contact-text { padding-right: 12px; }

  /* Back */
  .card-back {
    background: linear-gradient(135deg, var(--blue-deep), var(--blue-mid) 55%, var(--blue-light));
  }
  .back-panel {
    position: absolute; left: 12px; right: 12px; top: 12px; height: 400px;
    background: var(--card-white);
    display: flex; align-items: center; justify-content: center;
  }
  .cert-badge {
    position: absolute; left: 50%; bottom: 40px; transform: translateX(-50%);
    width: 76px; height: 76px; border-radius: 50%;
    border: 3px solid rgba(255,255,255,0.85);
  }
</style>
</head>
<body>
<main class="sheet">

  <section class="card card-front" aria-label="Card front">
    <div class="front-top">
      <div class="brand">
        <span class="brand-dot"></span>
        <span class="brand-name">TRASK<br>AERIAL IMAGING</span>
      </div>
    </div>

    <div class="name-band">
      <div class="icon-cell">
        <svg viewBox="0 0 24 24" aria-hidden="true"><circle cx="12" cy="8" r="5"/><path d="M2 23c0-6 4.5-9 10-9s10 3 10 9z"/></svg>
      </div>
      <div class="name-block">
        <span class="person-name">Daniel Trask</span>
        <span class="person-role">Owner/Operator</span>
      </div>
    </div>

    <ul class="contact-list">
      <li class="contact-row">
        <div class="icon-cell">
          <svg viewBox="0 0 24 24" aria-hidden="true"><path d="M7 1h10a2 2 0 0 1 2 2v18a2 2 0 0 1-2 2H7a2 2 0 0 1-2-2V3a2 2 0 0 1 2-2zm0 3v14h10V4z"/></svg>
        </div>
        <span class="contact-text">314-555-0187</span>
      </li>
      <li class="contact-row">
        <div class="icon-cell">
          <svg viewBox="0 0 24 24" aria-hidden="true" fill="none"><g fill="none" stroke="#fff" stroke-width="1.6"><circle cx="12" cy="12" r="10"/><ellipse cx="12" cy="12" rx="4.5" ry="10"/><path d="M2 12h20M4 6.5h16M4 17.5h16"/></g></svg>
        </div>
        <span class="contact-text">djtrask@skymail.net</span>
      </li>
      <li class="contact-row">
        <div class="icon-cell">
          <svg viewBox="0 0 24 24" aria-hidden="true"><path d="M12 2 1 12h3v10h6v-6h4v6h6V12h3z"/></svg>
        </div>
        <span class="contact-text">40528 Birchwood Ct.<br>Harlow Springs KS 63514</span>
      </li>
    </ul>
  </section>

  <section class="card card-back" aria-label="Card back">
    <div class="back-panel">
      <div class="brand">
        <span class="brand-dot"></span>
        <span class="brand-name">TRASK<br>AERIAL IMAGING</span>
      </div>
    </div>
    <div class="cert-badge" role="img" aria-label="Certification badge"></div>
  </section>

</main>
</body>
</html>
```